The Lantern and the Meadow: Songs Of Quiet Bloom

We need a book cover/spine and back cover for a multi author book called the Lantern and The Meadow: Songs of Quiet Bloom. This will be a collection of stories from women who major transformational stories to tell. They embark on a voyage, find themselves in uncharted territory, find friends or allies and in the end find themselves back home to themselves. I want this book cover to feel fun of wonder, adventure, intrigue with a a dainty energy. I have uploaded some images for inspiration but not to use in the design because they are not images I have permission to use.

```html
<!DOCTYPE html>
<html lang="en">
<head>
<meta charset="UTF-8">
<title>The Lantern and the Meadow: Songs of Quiet Bloom – Cover Wrap</title>
<link href="https://fonts.googleapis.com/css2?family=Roboto:ital,wght@0,400;0,500;0,700;1,500;1,700&family=Petit+Formal+Script&display=swap" rel="stylesheet">
<style>
  :root {
    --stage: #2a2a2c;
    --cover: #d4dae5;
    --cover-light: #dfe4ec;
    --purple: #5a2a7c;
    --crimson: #cf2a52;
    --ink: #22222c;
    --meadow-top: #c9cfdc;
    --meadow-mid: #a99bc6;
    --meadow-low: #7d5f9e;
    --portrait: #8d939e;
  }
  * { margin: 0; padding: 0; box-sizing: border-box; }
  html, body { width: 1200px; height: 800px; overflow: hidden; }
  body {
    background: var(--stage);
    font-family: "Roboto", Arial, sans-serif;
    color: var(--ink);
    display: flex;
    align-items: center;
    justify-content: center;
  }
  .cover-wrap {
    display: flex;
    height: 700px;
    box-shadow: 0 14px 40px rgba(0,0,0,.45);
  }

  /* Back cover */
  .back-cover {
    width: 470px;
    background: var(--cover);
    padding: 36px 34px 30px;
    position: relative;
  }
  .back-title {
    text-align: center;
    font-size: 25px;
    font-weight: 500;
    color: var(--purple);
    line-height: 1.1;
  }
  .back-title .lead { font-style: italic; font-weight: 700; }
  .back-title .key { color: var(--crimson); font-weight: 700; }
  .back-subtitle {
    text-align: center;
    font-family: "Petit Formal Script", cursive;
    color: var(--crimson);
    font-size: 15px;
    line-height: 1.6;
    margin-top: 4px;
  }
  .back-rule {
    width: 62%;
    height: 2px;
    margin: 6px auto 16px;
    background: linear-gradient(90deg, transparent, var(--purple) 20%, var(--purple) 80%, transparent);
  }
  .blurb {
    font-size: 10.5px;
    line-height: 1.5;
    text-align: justify;
    margin-bottom: 8px;
  }
  .section-heading {
    color: var(--crimson);
    font-size: 15px;
    font-weight: 500;
    margin: 14px 0 6px;
  }
  .learn-list { list-style: none; }
  .learn-list li {
    font-size: 10.5px;
    line-height: 1.6;
    padding-left: 10px;
    position: relative;
  }
  .learn-list li::before {
    content: "";
    position: absolute;
    left: 0; top: 6px;
    width: 5px; height: 5px;
    border-radius: 50%;
    background: var(--crimson);
  }
  .about-author {
    display: flex;
    gap: 12px;
    margin-top: 14px;
  }
  .author-portrait {
    width: 118px;
    height: 200px;
    flex-shrink: 0;
    background: linear-gradient(180deg, var(--cover) 0%, var(--portrait) 45%, #5b616c 100%);
    border-radius: 4px 4px 0 0;
  }
  .about-author .section-heading { margin: 0 0 4px; }
  .author-bio { font-size: 10px; line-height: 1.5; }
  .isbn-box {
    position: absolute;
    right: 34px;
    bottom: 30px;
    width: 128px;
    height: 58px;
    background: var(--purple);
    color: #fff;
    font-size: 30px;
    display: flex;
    align-items: center;
    justify-content: center;
  }

  /* Spine */
  .spine {
    width: 56px;
    background: var(--cover-light);
    border-left: 1px solid #c3c9d4;
    border-right: 1px solid #c3c9d4;
    display: flex;
    flex-direction: column;
    align-items: center;
    justify-content: space-between;
    padding: 60px 0 50px;
  }
  .spine-text {
    writing-mode: vertical-rl;
    white-space: nowrap;
  }
  .spine-title { font-size: 17px; font-weight: 500; color: var(--purple); }
  .spine-title .lead { font-style: italic; }
  .spine-title .key { color: var(--crimson); font-weight: 700; }
  .spine-author { font-size: 13px; letter-spacing: 2px; color: var(--purple); }

  /* Front cover */
  .front-cover {
    width: 470px;
    background: var(--cover);
    position: relative;
    text-align: center;
    overflow: hidden;
  }
  .front-text {
    position: relative;
    z-index: 1;
  }
  .front-author {
    padding-top: 46px;
    font-size: 32px;
    font-weight: 500;
    letter-spacing: 4px;
    color: var(--purple);
  }
  .front-title {
    margin-top: 40px;
    font-size: 66px;
    font-weight: 700;
    line-height: 1.08;
    color: var(--purple);
  }
  .front-title .lead { font-style: italic; font-weight: 500; }
  .front-title .key { color: var(--crimson); }
  .front-title .joiner { display: block; font-weight: 500; }
  .front-subtitle {
    font-family: "Petit Formal Script", cursive;
    color: var(--crimson);
    font-size: 25px;
    line-height: 1.6;
    margin-top: 2px;
  }
  .meadow-scene {
    position: absolute;
    left: 0; right: 0; bottom: 0;
    height: 300px;
    background: linear-gradient(180deg, var(--cover) 0%, var(--meadow-top) 40%, var(--meadow-mid) 72%, var(--meadow-low) 100%);
  }
</style>
</head>
<body>
  <main class="cover-wrap">
    <section class="back-cover">
      <h2 class="back-title"><span class="lead">The</span> <span class="key">LANTERN</span> And <span class="lead">The</span> <span class="key">MEADOW</span></h2>
      <p class="back-subtitle">Songs of Quiet Bloom</p>
      <div class="back-rule"></div>
      <p class="blurb">Lorem Ipsum is simply dummy text of the printing and typesetting industry. Lorem Ipsum has been the industry's standard dummy text ever since the 1500s, when an unknown printer took a galley of type and scrambled.</p>
      <p class="blurb">Lorem Ipsum is simply dummy text of the printing and typesetting industry. Lorem Ipsum has been the industry's standard dummy text ever since the 1500s, when an unknown printer took a galley of type and scrambled. Lorem Ipsum is simply dummy text of the printing and typesetting industry. Lorem Ipsum has been the industry's standard dummy text ever since the 1500s,</p>
      <h3 class="section-heading">Readers Will Learn :</h3>
      <ul class="learn-list">
        <li>Lorem Ipsum is simply printing and typesetting industry.</li>
        <li>Simply printing and typesetting industry.</li>
        <li>Printing and typesetting industry.</li>
        <li>Ipsum is simply printing and typesetting industry.</li>
        <li>Lorem Ipsum is simply printing and typesetting industry.</li>
        <li>Simply printing and typesetting industry.</li>
        <li>Printing and typesetting industry.</li>
        <li>Ipsum is simply printing and typesetting industry.</li>
      </ul>
      <div class="about-author">
        <div class="author-portrait" role="img" aria-label="Portrait photo of the author in a grey suit"></div>
        <div class="about-text">
          <h3 class="section-heading">About The Author</h3>
          <p class="author-bio">Lorem Ipsum is simply dummy text of the printing and typesetting industry. Lorem Ipsum has been the industry's standard dummy text ever since the 1500s, when an unknown printer took a galley of type and scrambled. Lorem Ipsum is simply dummy text of the printing and typesetting industry.</p>
        </div>
      </div>
      <div class="isbn-box">ISBN</div>
    </section>

    <section class="spine">
      <span class="spine-text spine-title"><span class="lead">The</span> <span class="key">LANTERN</span> And <span class="lead">The</span> <span class="key">MEADOW</span></span>
      <span class="spine-text spine-author">AUTHOR NAME</span>
    </section>

    <section class="front-cover">
      <div class="meadow-scene" role="img" aria-label="Photo of a girl with a flower crown and open arms standing in a field of lavender blossoms"></div>
      <div class="front-text">
        <p class="front-author">AUTHOR NAME</p>
        <h1 class="front-title">
          <span class="lead">The</span> <span class="key">LANTERN</span>
          <span class="joiner">And</span>
          <span class="lead">The</span> <span class="key">MEADOW</span>
        </h1>
        <p class="front-subtitle">Songs of Quiet Bloom</p>
      </div>
    </section>
  </main>
</body>
</html>
```